thornbury good buys

i want a creative logo,and a webpage that looks like a e-commerce with a inner city,or a rural background, or anything that makes you notice the page,there is no limit to the creativity,it would have 8 categories,jewlry=3pgs,beauty=3pgs,kids baby-toy=2pgs,shirts=2pgs,shoes=2pgs,gaming=2pgs,watches=2pgs. all credit cards plus coinvaro acceptable,17 page total,the last page for secure billing.if there are any questions im here for you.

Target Market(s)

my target market is people that just might find something they like for a reasonable price

Industry/Entity Type

E-Commerce

Requirements
Must have
• payment options are a must,they set the table for everything
Nice to have
• items mentioned above plus creativity

```html
<!DOCTYPE html>
<html lang="en">
<head>
<meta charset="utf-8">
<title>Thornbury Good Buys</title>
<link rel="stylesheet" href="https://fonts.googleapis.com/css2?family=Arimo:wght@400;700&family=Roboto+Condensed:wght@400;700&display=swap">
<style>
:root{
  --page:#ede4f7;
  --band:#d494f8;
  --panel:#e4d2f5;
  --panel-deep:#d6b2ef;
  --violet:#b03ee6;
  --plum:#5a2a78;
  --strip:#5b2a7e;
  --magenta:#d43fc4;
  --nav:#dcc0f2;
  --nav-text:#6a3d8c;
  --ink:#55505c;
  --amber:#fbc548;
  --amber-deep:#f5a722;
  --rule:#c2b8cb;
  --white:#ffffff;
}
*{box-sizing:border-box;margin:0;padding:0}
html,body{width:1192px;height:1200px;overflow:hidden;background:var(--page)}
body{font-family:"Arimo",Arial,sans-serif;color:var(--ink)}
.stage{position:relative;width:1024px;height:1031px;transform:scale(1.1641,1.1639);transform-origin:0 0;background:var(--page)}
.abs{position:absolute}

.top-band{left:0;top:0;width:1024px;height:18px;background:var(--band)}

.hero{left:113px;top:18px;width:802px;height:530px;overflow:hidden}
.hero svg{display:block}

.site-search{left:695px;top:34px;display:flex;gap:6px}
.site-search .field{width:168px;height:18px;border-radius:9px;background:var(--white);border:1px solid #cdb7e4;font-size:11px;font-style:italic;color:#9a93a3;padding:2px 8px}
.site-search .go{width:36px;height:18px;border-radius:5px;background:linear-gradient(#d9a7f7,#a966d8);color:var(--white);font-size:11px;text-align:center;line-height:18px;border:1px solid #fff}

.brand{left:137px;top:66px}
.brand-name{display:flex;align-items:center;gap:8px;font-size:33px;color:var(--violet);font-weight:400;letter-spacing:-.5px}
.brand-mark{width:14px;height:14px;background:var(--white)}
.brand-tag{margin-top:4px;margin-left:4px;width:168px;height:21px;background:var(--white);color:var(--violet);font-size:16px;letter-spacing:3px;text-align:center;line-height:21px}
.brand-slogan{margin-top:10px;margin-left:8px;font-size:21px;color:var(--white);letter-spacing:-.3px}

.main-nav{left:812px;top:127px;width:102px;list-style:none}
.main-nav li{height:23px;margin-bottom:5px;background:linear-gradient(#ead8f8,var(--nav));border:1px solid #f4eafc;border-radius:3px 0 0 3px;display:flex;align-items:center;font-family:"Roboto Condensed",sans-serif;font-size:14px;color:var(--nav-text)}
.main-nav li .ico{width:13px;height:13px;margin:0 9px 0 6px;border-radius:2px;background:#8a6aa8}
.main-nav li.active{background:linear-gradient(#e68ce6,var(--magenta));color:var(--white);justify-content:flex-start}
.main-nav li.active .ico{background:var(--white);margin-right:30px}

.tile{width:111px;height:111px;background:var(--white);border:1px solid #c9b3dc;border-radius:8px;display:flex;overflow:hidden}
.tile .photo{flex:1;margin:5px}
.tile .label{width:15px;background:var(--strip);color:var(--white);writing-mode:vertical-rl;text-orientation:upright;font-size:13px;letter-spacing:1px;display:flex;align-items:center;justify-content:center;border-radius:0 7px 7px 0}
.jewelry .photo{background:linear-gradient(135deg,#e9e2d2,#c9b178 50%,#e4e4ea)}
.beauty .photo{background:linear-gradient(135deg,#f6c0b8,#e04a3c 50%,#c9233e)}
.toys .photo{background:radial-gradient(circle at 50% 50%,#f2c8a4,#7b95b4 70%,#fff)}
.shirts .photo{background:linear-gradient(#9a6d48,#6e4a2e)}
.shoes .photo{background:radial-gradient(circle,#b7bcc3,#6f7782 60%,#fff 80%)}
.pants .photo{background:linear-gradient(90deg,#5b5f6a,#d8cbb0 50%,#233452)}
.gaming .photo{background:radial-gradient(circle,#3b4250,#161a22 55%,#fff 75%)}
.watches .photo{background:radial-gradient(circle,#dcdde0,#8a6b4f 55%,#fff 75%)}

.login{left:770px;top:426px;width:138px}
.login-title{font-size:13px;font-weight:700;color:#1b1b22;margin-left:68px;display:flex;align-items:center;gap:6px}
.login-title .lock{width:11px;height:10px;background:var(--amber-deep);border-radius:2px;border-top:3px solid #c98b16}
.login .field{display:block;width:134px;height:15px;margin-top:9px;border-radius:8px;background:var(--white);border:1px solid #d6bfe8;font-size:11px;color:#a49aae;text-align:center;line-height:13px}
.login .field+.field{margin-top:16px}
.login .btn{margin:10px 0 0 58px;width:76px;height:17px;background:linear-gradient(#e37de0,#a6269f);border-radius:3px;color:var(--white);font-size:11px;font-weight:700;text-align:center;line-height:17px}
.login .links{margin-top:5px;font-size:10px;color:#3c3344;text-decoration:underline;white-space:nowrap}
.padlock{left:710px;top:498px;width:24px;height:32px}

.shop-bar{left:114px;top:550px;width:802px;height:55px;border-radius:6px;background:linear-gradient(#fde08f,var(--amber) 50%,var(--amber-deep));border:1px solid #f0b24a}
.dept{left:14px;top:14px;width:161px;height:27px;border-radius:4px;background:linear-gradient(#fbfbfb,#d3d3d3);border:1px solid #9c9c9c;font-family:"Roboto Condensed",sans-serif;font-size:14px;color:#222;padding:5px 0 0 11px}
.caret{position:absolute;right:3px;top:3px;width:23px;height:19px;background:linear-gradient(#fafafa,#cfcfcf);border:1px solid #999}
.caret::after{content:"";position:absolute;left:6px;top:6px;border-left:5px solid transparent;border-right:5px solid transparent;border-top:7px solid #333}
.search-label{left:198px;top:20px;font-family:"Roboto Condensed",sans-serif;font-size:14px;color:#222}
.search-select{left:248px;top:14px;width:204px;height:26px;background:var(--white);border:1px solid #aaa;border-radius:2px}
.search-input{left:479px;top:12px;width:258px;height:28px;background:var(--white);border:1px solid #bbb;border-radius:2px}
.search-go{left:756px;top:6px;width:40px;height:40px;border-radius:50%;background:radial-gradient(circle at 50% 30%,#f79ae8,var(--magenta) 60%,#a51b93);color:var(--white);font-size:17px;text-align:center;line-height:40px;border:2px solid #fde3a0}

.intro{left:116px;top:614px;width:786px;height:136px;overflow:hidden;font-size:12px;line-height:18px;letter-spacing:.35px;text-align:justify}
.intro h2{font-size:12.5px;font-weight:400;color:var(--violet);margin-bottom:6px}
.intro p{margin-bottom:2px}
.intro p.lead{text-indent:36px}

.footer-band{left:0;top:785px;width:1024px;height:150px;background:var(--band)}
.key-art{left:118px;top:800px;width:64px;height:54px;border-radius:24px 10px 24px 10px;background:linear-gradient(135deg,#ffffff,#8fd8f6 60%,#3aa3d8)}
.signup{left:190px;top:812px;color:var(--white)}
.signup h3{font-size:18px;font-weight:400}
.signup p{font-size:11px;font-weight:700;color:#5a2a78;margin-top:1px}
.email{left:118px;top:876px;width:292px;height:40px;background:var(--white);border-radius:6px;border:2px solid #e9d3fb;font-size:17px;color:#c9c3d0;padding:9px 0 0 31px;letter-spacing:.3px}
.email .arrow{position:absolute;right:6px;top:3px;width:30px;height:30px;border-radius:3px;background:linear-gradient(#fff,#d6d6d6);border:1px solid #9a9a9a}
.email .arrow::after{content:"";position:absolute;left:11px;top:9px;border-top:5px solid transparent;border-bottom:5px solid transparent;border-left:7px solid #555}
.divider{left:518px;top:797px;height:116px;border-left:1px dashed #f3e2ff}
.follow{left:665px;top:803px;color:var(--white);font-size:12px}
.social{left:666px;top:835px;display:flex;gap:6px}
.social span{width:44px;height:44px;border-radius:50%;background:var(--white);border:2px solid #efe1fb;color:var(--plum);font-size:9.5px;font-weight:700;display:flex;align-items:center;justify-content:center}
.social span:last-child{margin-left:4px}

.links{left:0;top:962px;width:1024px;text-align:center;font-size:12px;color:#3c3744}
.links a{color:inherit;text-decoration:none}
.links i{font-style:normal;margin:0 6px}
.copyright{left:0;top:1001px;width:1024px;height:30px;background:var(--rule);text-align:center;line-height:30px;font-size:12px;color:#3a3540;letter-spacing:.4px}
</style>
</head>
<body>
<div class="stage">
  <div class="abs top-band"></div>

  <div class="abs hero">
    <svg width="802" height="530" viewBox="0 0 802 530">
      <defs>
        <linearGradient id="heroBg" x1="0" y1="0" x2="0" y2="1">
          <stop offset="0" stop-color="#ece0f8"/>
          <stop offset="1" stop-color="#e2cdf4"/>
        </linearGradient>
        <radialGradient id="bloom" cx=".3" cy=".35" r=".7">
          <stop offset="0" stop-color="#f6f0fc"/>
          <stop offset=".45" stop-color="#d9bdf0"/>
          <stop offset="1" stop-color="#c79de8"/>
        </radialGradient>
      </defs>
      <rect width="802" height="530" fill="url(#heroBg)"/>
      <path role="img" aria-label="Soft close-up of a lilac flower" d="M0,0 H802 V67 C650,170 460,225 340,220 C210,214 90,180 0,132 Z" fill="url(#bloom)"/>
      <path d="M0,132 C90,180 210,214 340,220 C460,225 650,170 802,67" fill="none" stroke="#ffffff" stroke-width="3"/>
      <path d="M0,455 C110,505 260,528 420,530 H0 Z" fill="#dcbcef"/>
      <path d="M540,530 C640,520 650,440 720,400 C760,385 790,380 802,382 V530 Z" fill="var(--panel-deep)"/>
    </svg>
  </div>

  <form class="abs site-search">
    <div class="field">search....</div>
    <div class="go">GO</div>
  </form>

  <div class="abs brand">
    <div class="brand-name"><span class="brand-mark"></span>Thornbury</div>
    <div class="brand-tag">Good Buys</div>
    <div class="brand-slogan">Slogan Text Here</div>
  </div>

  <ul class="abs main-nav">
    <li class="active"><span class="ico"></span>Home</li>
    <li><span class="ico"></span>About Us</li>
    <li><span class="ico"></span>Products</li>
    <li><span class="ico"></span>Services</li>
    <li><span class="ico"></span>Account</li>
    <li><span class="ico"></span>Contact Us</li>
  </ul>

  <div class="abs tile jewelry" style="left:115px;top:221px"><div class="photo" role="img" aria-label="Gold and silver bangles"></div><div class="label">Jewelry</div></div>
  <div class="abs tile beauty" style="left:115px;top:348px"><div class="photo" role="img" aria-label="Lipsticks in red tones"></div><div class="label">Beauty</div></div>
  <div class="abs tile toys" style="left:292px;top:257px"><div class="photo" role="img" aria-label="Soft toy doll"></div><div class="label">Toys</div></div>
  <div class="abs tile shirts" style="left:292px;top:381px"><div class="photo" role="img" aria-label="Brown button shirt"></div><div class="label">Shirts</div></div>
  <div class="abs tile shoes" style="left:476px;top:252px"><div class="photo" role="img" aria-label="Running shoe"></div><div class="label">Shoes</div></div>
  <div class="abs tile pants" style="left:479px;top:381px"><div class="photo" role="img" aria-label="Three pairs of trousers"></div><div class="label">Pants</div></div>
  <div class="abs tile gaming" style="left:658px;top:201px"><div class="photo" role="img" aria-label="Gaming keypad"></div><div class="label">Gaming</div></div>
  <div class="abs tile watches" style="left:658px;top:335px"><div class="photo" role="img" aria-label="Pair of wrist watches"></div><div class="label">Watches</div></div>

  <svg class="abs padlock" viewBox="0 0 24 32" aria-hidden="true">
    <path d="M5,14 V9 a7,7 0 0 1 14,0 V14" fill="none" stroke="#9a9a9a" stroke-width="3"/>
    <rect x="1" y="13" width="22" height="18" rx="2" fill="#f6b41f"/>
    <rect x="1" y="22" width="22" height="6" fill="#3a3a3a"/>
  </svg>

  <form class="abs login">
    <div class="login-title">LOGIN <span class="lock"></span></div>
    <div class="field">User name</div>
    <div class="field">Pass word</div>
    <div class="btn">LOGON</div>
    <div class="links">New user / Forget Pass word</div>
  </form>

  <div class="abs shop-bar">
    <div class="abs dept">Shop All Depotments<span class="caret"></span></div>
    <div class="abs search-label">Search</div>
    <div class="abs search-select"><span class="caret"></span></div>
    <div class="abs search-input"></div>
    <div class="abs search-go">GO</div>
  </div>

  <section class="abs intro">
    <h2>Some shopping carts get your business online in no time.</h2>
    <p class="lead">If you're new to selling online and you're just starting out, you'll want a shopping cart service that handles all the details of creating an online store, including:Registering a website nameBuilding and hosting your siteOnline marketingWhen it comes to accepting credit cards online, find a shopping cart that supports our Coinvaro Payments Standard product – it's the fastest and easiest way to start getting paid online. You can literally accept online payments in less than 15 minutes—with no advanced programming skills required.</p>
    <p>If you're new to selling online and you're just starting out, you'll want a shopping cart service that handles all the details of creating an online store, including:Registering a website nameBuilding and hosting your siteOnline marketingWhen it comes to accepting credit cards online, find a shopping cart that supports our payments product.</p>
  </section>

  <div class="abs footer-band"></div>
  <div class="abs key-art" role="img" aria-label="Blue key with tag"></div>
  <div class="abs signup">
    <h3>Sign up for Thornbury news</h3>
    <p>and receive 10% off your next order!</p>
  </div>
  <div class="abs email">ENTER EMAIL ID<span class="arrow"></span></div>
  <div class="abs divider"></div>
  <div class="abs follow">follow on us</div>
  <div class="abs social">
    <span>Kwibble</span><span>Folkly</span><span>Jotlog</span><span>Mingly</span><span>Linkwork</span>
  </div>

  <nav class="abs links">
    <a>About Us</a><i>|</i><a>Contact Us</a><i>|</i><a>Store Finder</a><i>|</i><a>Careers</a><i>|</i><a>PressBlog</a><i>|</i><a>News</a><i>|</i><a>Privacy</a><i>|</i><a>Accessibility</a>
  </nav>
  <div class="abs copyright">Copyright © 2010 THORNBURY. All rights reserved.</div>
</div>
</body>
</html>
```